Custom Header Designs - Automotive Parts - Alternator & Starter

We need 8 Header/Hero designs that will be used on our website. We are a company based in Montreal Canada and we re-manufacture Alternators and Starters for all types of vehicles. We offer a premium product and we are looking for premium designs that reflect the look of our packaging and the look of our website. Essentially we specialize in the sale and manufacture of two specific parts that go on all types of vehicles, Alternators and Starters. All text on these designs need to be editable as we will need to translate them to French once we get the source files.
Here are some websites of our competitors so you can draw some inspiration and see what our industry/business is all about:
https://www.quellorn.com/
https://www.rivetanvil.com/
Article that describes a remanufactured product, https://www.zephtrove.com/articles/starters-and-alternators-reman-vs-new.html
Our packaging is modern, sleek and professional. Our website is a B2B E-Commerce Site as well as an info site to promote our products. It is clean and minimal but we want the header/hero designs to help it stand out. Our main colors are blue and gray (as seen in our logo), but you can use whatever you like to compliment these colors.
Our packaging design was done on PixelHarbor, here is the link to that project so that you can see the packaging look and use any of the info that is from that project.
https://jobs.pixelharbor.ca/job/5820467
The 8 Header/Hero designs will be used in the following areas, I have included a brief description of what we are looking for:
1 - Homepage Header/Hero image - This will be the homepage hero image therefore it should summarize the info described below. We offer premium quality re-manufactured alternators and starters. We are a wholesaler/distributor that services major auto-part stores with these quality products.
2 - General Product Header/Hero image - This image will be used as a header where the customer can learn general info about our products and any custom work we can do. This page will have a section where you can click to learn more about our individual product lines (links to product specific pages mentioned below) and a description of the custom work we can perform. We offer a two year manufacturers warranty.
3 - Alternator Product Header/Hero image - This image will be used to showcase our Alternator Product Line. Its purpose is to promote and advertise our premium re-manufactured alternators. This page will provide detailed info about our alternator re-manufacturing process and describe why our alternators are great.
4 - Starter Product Header/Hero image - This image will be used to showcase our Starter Product Line. Its purpose is to promote and advertise our premium re-manufactured starters. This page will provide detailed info about our starter re-manufacturing process and describe why our starters are great.
5 - General Header/Hero Image - This image will be used in most of our standard pages like our terms and conditions, privacy policy, warranty policy, our company page, etc. It needs to relate to the industry but be general enough so that we could use it in multiple areas
6 - Online Ordering Header image - This image will be used in our B2B area to introduce our customers to the Online Ordering system, its purpose is to advertise and explain some of the features of the Online Ordering system.
7 - B/O Re-Manufacture & Return Header Image - This image will be used in our B2B area to explain and advertise to our customers how our Backorder/R&R process works on our website. Essentially if we do not have the remanufactured part in stock but we have the core you could put the product on Backorder and we will remanufacture it in a few hours. If for any reason (rare vehicle, old vehicle, etc.) we do not have the core we will R&R (Remanufacture and Return) the customers core for them.
8 - Bulk Ordering Form Header Image - This image will be used in our B2B area to explain and advertise to our customers how our Bulk Ordering Form works on our website.
These hero/header images will be going on a Wordpress/WooCommerce website and I am suggesting these images have a size of 1600 x 500, but we will take any other suggestions from the designers as you are the experts.
I have included a zip file that includes images of various elements that will help you in the design process.
Target Market(s)
Educate consumers about our products and attract auto supply chains to become distributors of our products.
Industry/Entity Type
Automotive Part

```html
<!DOCTYPE html>
<html lang="en">
<head>
<meta charset="utf-8">
<title>Kelvara – Alternators</title>
<link rel="stylesheet" href="https://fonts.googleapis.com/css2?family=Arimo:wght@400;700&family=Bebas+Neue&family=Raleway:wght@200&display=swap">
<style>
  :root {
    --topbar-bg: #f2f2f2;
    --link-blue: #3d5ca8;
    --brand-blue: #1d3f9a;
    --nav-text: #5a5a5a;
    --ink: #08111f;
    --navy-deep: #0b1f3d;
    --navy-mid: #22457a;
    --mist: #dfe8f3;
    --band-dark: #050b14;
    --band-navy: #0b1a2d;
    --sub-grey: #b9bec6;
    --badge: #9fd6ee;
    --metal-light: #e7eaee;
    --metal-dark: #7d8590;
  }
  * { margin: 0; padding: 0; box-sizing: border-box; }
  html, body { width: 1200px; height: 794px; overflow: hidden; background: #fff; }
  body { position: relative; font-family: "Arimo", Arial, sans-serif; }

  .top-bar { position: absolute; left: 0; top: 0; width: 1200px; height: 29px; background: var(--topbar-bg); font-size: 12px; }
  .top-bar span { position: absolute; top: 7px; white-space: nowrap; }
  .top-bar .consult { left: 94px; color: var(--link-blue); }
  .top-bar .phone { left: 554px; color: #8a8a8a; }
  .top-bar .phone b { color: #333; }
  .top-bar .sep { left: 715px; color: #999; }
  .top-bar .map { left: 733px; color: var(--link-blue); }
  .top-bar .dashboard { left: 881px; top: 9px; font-size: 10px; color: var(--brand-blue); letter-spacing: .2px; }
  .top-bar .lang { left: 1036px; top: 8px; font-size: 10px; color: #444; display: flex; align-items: center; gap: 3px; }
  .lang-mark { width: 15px; height: 10px; background: #2a3f8f; display: inline-block; }

  .site-header { position: absolute; left: 0; top: 29px; width: 1200px; height: 90px; background: #fff; }
  .brand { position: absolute; left: 105px; top: 24px; display: flex; align-items: center; gap: 10px; }
  .brand-dot { width: 40px; height: 40px; border-radius: 50%; background: var(--brand-blue); }
  .brand-name { font-family: "Arimo", Arial, sans-serif; font-weight: 700; font-size: 30px; color: var(--brand-blue); }
  .main-nav a { position: absolute; top: 35px; font-size: 13.5px; color: var(--nav-text); text-decoration: none; white-space: nowrap; }
  .cart { position: absolute; left: 1073px; top: 36px; }
  .cart-badge { position: absolute; left: 1092px; top: 27px; width: 17px; height: 17px; border-radius: 50%; background: var(--badge); color: #2c4c7a; font-size: 9px; line-height: 17px; text-align: center; }

  .hero { position: absolute; left: 0; top: 119px; width: 1200px; height: 508px; overflow: hidden; }
  .hero-bg { position: absolute; inset: 0; }
  .hero-product { position: absolute; left: 706px; top: 115px; width: 335px; height: 288px; border-radius: 46% 40% 44% 48%;
    background: radial-gradient(circle at 40% 45%, var(--metal-light), #b9bfc7 55%, var(--metal-dark)); }
  .hero-title { position: absolute; left: 194px; top: 200px; font-family: "Bebas Neue", "Oswald", sans-serif; font-size: 95px; line-height: 1; color: var(--ink); letter-spacing: 1px; }
  .hero-rule { position: absolute; left: 188px; top: 293px; width: 524px; height: 2px; background: var(--navy-deep); }
  .hero-sub { position: absolute; left: 391px; top: 302px; font-family: "Raleway", sans-serif; font-weight: 200; font-size: 40px; line-height: 1; color: #111; }

  .product-band { position: absolute; left: 0; top: 627px; width: 1200px; height: 167px; background: linear-gradient(180deg, var(--band-dark), var(--band-navy)); }
  .product-divider { position: absolute; top: 23px; width: 1px; height: 119px; background: #2a3442; }
  .product-card { position: absolute; top: 0; height: 167px; }
  .product-name { position: absolute; top: 33px; font-weight: 700; font-size: 19.5px; line-height: 27px; color: #fff; white-space: nowrap; }
  .product-subname { position: absolute; top: 88px; font-size: 18.5px; color: var(--sub-grey); white-space: nowrap; }
  .product-image { position: absolute; border-radius: 44%;
    background: radial-gradient(circle at 40% 45%, var(--metal-light), #a9afb8 60%, #4d545e); }
</style>
</head>
<body>
  <div class="top-bar">
    <span class="consult">Book a Sales Consultation →</span>
    <span class="phone">Call us now: <b>555.018.4420</b></span>
    <span class="sep">|</span>
    <span class="map">Find us on the map →</span>
    <span class="dashboard">MY KELVARA DASHBOARD</span>
    <span class="lang"><i class="lang-mark"></i>English (English)</span>
  </div>

  <header class="site-header">
    <div class="brand"><span class="brand-dot"></span><span class="brand-name">Kelvara</span></div>
    <nav class="main-nav">
      <a style="left:356px">Home</a>
      <a style="left:414px">Products</a>
      <a style="left:489px">Our Company</a>
      <a style="left:594px">Customer Resources</a>
      <a style="left:742px">Contact Us</a>
      <a style="left:831px">Online Ordering</a>
      <a style="left:947px">Hello, administrator</a>
    </nav>
    <svg class="cart" width="22" height="22" viewBox="0 0 22 22" aria-label="Cart">
      <path d="M3 9h16l-1.5 11h-13z" fill="none" stroke="#444" stroke-width="1.6"/>
      <path d="M7 9V6a4 4 0 0 1 8 0v3" fill="none" stroke="#444" stroke-width="1.6"/>
    </svg>
    <span class="cart-badge">2</span>
  </header>

  <section class="hero">
    <svg class="hero-bg" width="1200" height="508" viewBox="0 0 1200 508" role="img" aria-label="Sports car photographed in a misty blue setting behind a diagonal split">
      <defs>
        <linearGradient id="darkSide" x1="0" y1="0" x2="1" y2="1">
          <stop offset="0" stop-color="#2a518a"/>
          <stop offset="1" stop-color="#0a1c36"/>
        </linearGradient>
        <linearGradient id="lightSide" x1="0" y1="0" x2="1" y2="1">
          <stop offset="0" stop-color="#aec3dc"/>
          <stop offset=".55" stop-color="#eef3f9"/>
          <stop offset="1" stop-color="#c9d6e6"/>
        </linearGradient>
      </defs>
      <rect width="1200" height="508" fill="url(#darkSide)"/>
      <polygon points="291,0 1003,0 666,508 0,508 0,334" fill="url(#lightSide)"/>
      <line x1="1110" y1="0" x2="740" y2="508" stroke="#0b1830" stroke-width="1"/>
    </svg>
    <div class="hero-product" role="img" aria-label="Heavy-duty alternator"></div>
    <h1 class="hero-title">ALTERNATORS</h1>
    <div class="hero-rule"></div>
    <p class="hero-sub">HEAVY-DUTY</p>
  </section>

  <section class="product-band">
    <div class="product-divider" style="left:384px"></div>
    <div class="product-divider" style="left:775px"></div>

    <div class="product-image" style="left:214px;top:-22px;width:152px;height:133px" role="img" aria-label="Alternator product"></div>
    <p class="product-name" style="left:68px">ALTERNATOR<br>NAME</p>
    <p class="product-subname" style="left:68px">Subname</p>

    <div class="product-image" style="left:586px;top:-24px;width:164px;height:141px" role="img" aria-label="Alternator product"></div>
    <p class="product-name" style="left:434px">ALTERNATOR<br>NAME</p>
    <p class="product-subname" style="left:434px">Subname</p>

    <div class="product-image" style="left:981px;top:-22px;width:153px;height:133px" role="img" aria-label="Alternator product"></div>
    <p class="product-name" style="left:834px">ALTERNATOR<br>NAME</p>
    <p class="product-subname" style="left:834px">Subname</p>
  </section>
</body>
</html>
```